Cosmetic Dentist Practice needs stationery package/logo

I need a letterhead, envelope and business card for a cosmetic and Dental Inplant practice in an upscale part of Houston. The business card will be a size 3.5 x 2 and the letterhead will be 8.5" x 11" with a standard #10 envelope.
I have uploaded a file with an idea that the dentist had for his cards. Please note that this is not the size that the card should be. It does provide the information required.
Updates
Thank you all for your submissions. They were each unique and special in their own way. My client has made a selection that he feels best meets his needs. I appreciate each of you taking the time to offer designs. Good luck to each of you...I hope to see you back in MarblePost on future projects.
Industry/Entity Type
Business
Look and feel
Each slider illustrates characteristics of the customer's brand and the style your logo design should communicate.

```html
<!DOCTYPE html>
<html lang="en">
<head>
<meta charset="utf-8">
<title>Letterhead – Marcus Leland, D.D.S.</title>
<link rel="stylesheet" href="https://fonts.googleapis.com/css2?family=Old+Standard+TT:wght@400;700&display=swap">
<style>
  :root {
    --paper: #ffffff;
    --ink: #111111;
    --page-bg: #ffffff;
  }
  html, body {
    margin: 0;
    padding: 0;
    background: var(--page-bg);
    overflow: hidden;
  }
  .letterhead {
    position: relative;
    width: 927px;
    height: 1200px;
    background: var(--paper);
    color: var(--ink);
    overflow: hidden;
  }
  .letterhead__header {
    position: absolute;
    left: 0;
    top: 0;
    width: 927px;
    height: 130px;
  }
  .letterhead__header text {
    fill: var(--ink);
    font-family: "Old Standard TT", Georgia, serif;
    font-weight: 400;
  }
  .practice-details__address,
  .practice-details__contact {
    font-weight: 700;
  }
</style>
</head>
<body>
  <main class="letterhead">
    <svg class="letterhead__header" viewBox="0 0 927 130" role="group" aria-label="Marcus Leland, D.D.S., PLLC – Parkside Smile &amp; Implant Care">
      <g class="practice-details">
        <text class="practice-details__name" x="20" y="38" font-size="27" textLength="442" lengthAdjust="spacingAndGlyphs">MARCUS LELAND,D.D.S.,PLLC</text>
        <text class="practice-details__specialty" x="21" y="68" font-size="29" textLength="438" lengthAdjust="spacing">PROSTHODONTIST</text>
        <text class="practice-details__address" x="18" y="92" font-size="13" textLength="441" lengthAdjust="spacingAndGlyphs">48 Cedar Crest Lane Suite 210, W. Houston, TX 77031</text>
        <text class="practice-details__contact" x="53" y="116" font-size="13" textLength="173" lengthAdjust="spacingAndGlyphs">Phone: 713-555-0142</text>
        <text class="practice-details__contact" x="274" y="116" font-size="13" textLength="149" lengthAdjust="spacingAndGlyphs">Fax:713-555-0187</text>
      </g>
      <g class="brand-name">
        <text x="476" y="64" font-size="64" textLength="430" lengthAdjust="spacingAndGlyphs">PARKSIDE SMILE</text>
        <text x="476" y="116" font-size="64" textLength="430" lengthAdjust="spacingAndGlyphs">&amp; IMPLANT CARE</text>
      </g>
    </svg>
  </main>
</body>
</html>
```